PACKAGING DESIGN FOR ESSENTIAL OIL

The product is argan oil and I would be selling it in 30ml amber glass bottle.
I am looking for a design to put on the bottle. The brand name is LA BRUME (Amber Mist translated in english). I would be using screen printing for the design on the glass bottle.
The bottle would be put in a carton box and I would need a design for that as well. I would like the carton box to be in gold colour (but you can propose a design with any other colour for the carton as well).
I am sending a picture with measurements of the glass bottle with its cap on it.
I am also sending the details I want to be included on the carton box.
I would like a design related to Morocco as the argan oil is from Morocco.
I have uploaded images that can inspire you all for my design.
I am sending you as well a link from findpix for Moroccan Mosaic:
https://www.findpix-example.mu/search?q=argan+oil+brand&source=lnms&tbm=isch&sa=X&ei=aVZaUuKfFM7nrAeS7oGQAQ&ved=0CAcQ_AUoAQ&biw=1280&bih=658&dpr=1#q=moroccan+mosaic&tbm=isch&imgdii=_
Industry/Entity Type
Screen Printing
Requirements
Must have
- The Moroccan touch must be present in the design.
I would also like to have the brand name La Brume hot foil printed.
Nice to have
- A design of the argan tree would be nice as it shows exactly what we are selling.

```html
<!DOCTYPE html>
<html lang="fr">
<head>
<meta charset="utf-8">
<title>La Brume — Huile d'Argan Biologique</title>
<link href="https://fonts.googleapis.com/css2?family=Cinzel:wght@400;500&family=Pinyon+Script&display=swap" rel="stylesheet">
<style>
  :root {
    --gold: #d6b673;
    --gold-deep: #c9a862;
    --ivory: #ffffff;
    --ornament: rgba(255, 255, 255, 0.82);
  }
  html, body {
    margin: 0;
    padding: 0;
    overflow: hidden;
  }
  .canvas {
    position: relative;
    width: 1200px;
    height: 1000px;
    background: var(--gold);
    overflow: hidden;
  }
  .label-frame {
    position: absolute;
    inset: 0;
  }
  .label-text {
    position: absolute;
    left: 0;
    width: 1200px;
    text-align: center;
    color: var(--ivory);
    margin: 0;
  }
  .brand-name {
    top: 176px;
    font-family: "Cinzel", serif;
    font-weight: 500;
    font-size: 60px;
    letter-spacing: 2px;
    line-height: 1;
  }
  .product-name {
    top: 292px;
    font-family: "Pinyon Script", cursive;
    font-size: 50px;
    line-height: 1;
  }
  .product-grade {
    top: 370px;
    font-family: "Cinzel", serif;
    font-size: 19px;
    letter-spacing: 8px;
    line-height: 1;
  }
  .claim {
    top: 752px;
    font-family: "Cinzel", serif;
    font-size: 38px;
    letter-spacing: 3px;
    line-height: 1;
  }
  .volume {
    top: 804px;
    font-family: "Cinzel", serif;
    font-size: 19px;
    line-height: 1;
  }
</style>
</head>
<body>
<main class="canvas">
  <svg class="label-frame" width="1200" height="1000" viewBox="0 0 1200 1000">
    <defs>
      <pattern id="frame-hatch" width="3" height="3" patternUnits="userSpaceOnUse">
        <rect width="1.2" height="3" fill="var(--ivory)"/>
      </pattern>
    </defs>
    <!-- outer border with hatched band -->
    <path class="frame-outer" d="M357 137 H535 A65 65 0 0 1 665 137 H845 V862 H665 A65 65 0 0 1 535 862 H357 Z"
          fill="url(#frame-hatch)" stroke="var(--ivory)" stroke-width="4"/>
    <path class="frame-band-inner" d="M369 149 H541 A59 59 0 0 1 659 149 H833 V850 H659 A59 59 0 0 1 541 850 H369 Z"
          fill="var(--gold)" stroke="var(--ivory)" stroke-width="2"/>
    <!-- inner line with corner notches and arches -->
    <path class="frame-inner"
          d="M416 160 H552 A48 48 0 0 1 648 160 H784 A38 38 0 0 0 822 198 V802 A38 38 0 0 0 784 840 H648 A48 48 0 0 1 552 840 H416 A38 38 0 0 0 378 802 V198 A38 38 0 0 0 416 160 Z"
          fill="none" stroke="var(--ivory)" stroke-width="3"/>

    <!-- Moroccan rosette ornaments -->
    <g role="img" aria-label="Moroccan rosette ornament in the top arch">
      <circle cx="600" cy="124" r="30" fill="var(--ornament)"/>
    </g>
    <g role="img" aria-label="Moroccan rosette ornament in the bottom arch">
      <circle cx="600" cy="876" r="30" fill="var(--ornament)"/>
    </g>
    <g role="img" aria-label="Small Moroccan rosette ornaments in the four corners">
      <circle cx="386" cy="164" r="20" fill="var(--ornament)"/>
      <circle cx="818" cy="164" r="20" fill="var(--ornament)"/>
      <circle cx="386" cy="836" r="20" fill="var(--ornament)"/>
      <circle cx="818" cy="836" r="20" fill="var(--ornament)"/>
    </g>
    <g role="img" aria-label="Moroccan mosaic star medallion surrounded by eight small rosettes">
      <circle cx="600" cy="567" r="108" fill="var(--ornament)"/>
      <circle cx="600" cy="434" r="18" fill="var(--ornament)"/>
      <circle cx="600" cy="700" r="18" fill="var(--ornament)"/>
      <circle cx="470" cy="567" r="18" fill="var(--ornament)"/>
      <circle cx="730" cy="567" r="18" fill="var(--ornament)"/>
      <circle cx="510" cy="475" r="26" fill="var(--ornament)"/>
      <circle cx="694" cy="475" r="26" fill="var(--ornament)"/>
      <circle cx="510" cy="659" r="26" fill="var(--ornament)"/>
      <circle cx="694" cy="659" r="26" fill="var(--ornament)"/>
    </g>
  </svg>

  <h1 class="label-text brand-name">LA BRUME</h1>
  <p class="label-text product-name">Huile D’Argan</p>
  <p class="label-text product-grade">BIOLOGIQUE</p>
  <p class="label-text claim">100% NATUREL</p>
  <p class="label-text volume">30 ML</p>
</main>
</body>
</html>
```